Business Card Design for Korvana (Farming Devices)

We need Business Cards for our new Company based in Switzerland called "Korvana" We develop innovativ products for indoor and outdoor Farming for household and components for vertical farming. Our initial BloomNook gives people the possibility to grow their own food at home all year round. The design should communicate freshness, innovation, health.

```html
<!DOCTYPE html>
<html lang="en">
<head>
<meta charset="utf-8">
<title>Korvana Business Card</title>
<link href="https://fonts.googleapis.com/css2?family=Lato:ital,wght@0,400;0,700;1,400&display=swap" rel="stylesheet">
<style>
  :root {
    --backdrop: #9b9b9b;
    --card-white: #ffffff;
    --brand-blue: #006ebd;
    --brand-green: #76b543;
    --ink: #3a3a3a;
    --ink-soft: #555555;
  }
  html, body {
    margin: 0;
    padding: 0;
    width: 1133px;
    height: 1200px;
    overflow: hidden;
    background: var(--backdrop);
    font-family: "Lato", Arial, sans-serif;
  }
  .canvas {
    position: relative;
    width: 1133px;
    height: 1200px;
  }
  .card {
    position: absolute;
    border-radius: 24px;
    overflow: hidden;
  }
  .card-front {
    left: 197px;
    top: 144px;
    width: 724px;
    height: 412px;
    background: var(--card-white);
  }
  .card-back {
    left: 201px;
    top: 640px;
    width: 717px;
    height: 411px;
    background: var(--brand-blue);
  }
  .brand-name {
    position: absolute;
    left: 43px;
    top: 76px;
    margin: 0;
    font-size: 44px;
    font-weight: 400;
    line-height: 1;
    color: var(--brand-green);
    letter-spacing: 1px;
    text-transform: uppercase;
  }
  .person {
    position: absolute;
    left: 43px;
    top: 160px;
  }
  .person-name {
    margin: 0;
    font-size: 23px;
    font-weight: 700;
    line-height: 1.1;
  }
  .person-name .first { color: var(--brand-green); }
  .person-name .last { color: var(--brand-blue); }
  .person-role {
    margin: 1px 0 0;
    font-size: 16px;
    color: var(--ink);
  }
  .address {
    position: absolute;
    left: 44px;
    top: 226px;
    margin: 0;
    font-style: normal;
    font-size: 16px;
    line-height: 21px;
    color: var(--ink-soft);
  }
  .contact-list {
    position: absolute;
    left: 44px;
    top: 274px;
    margin: 0;
    padding: 0;
    list-style: none;
    font-size: 16px;
    line-height: 20.7px;
    color: var(--ink-soft);
  }
  .contact-list li {
    display: flex;
    align-items: center;
    gap: 10px;
  }
  .contact-icon {
    width: 14px;
    height: 14px;
    flex: none;
    fill: var(--brand-blue);
  }
  .front-band {
    position: absolute;
    left: 0;
    top: 0;
    width: 724px;
    height: 412px;
  }
  .website {
    position: absolute;
    left: 346px;
    top: 371px;
    margin: 0;
    font-size: 21px;
    font-style: italic;
    color: var(--card-white);
    letter-spacing: 0.2px;
  }
  .back-wordmark {
    position: absolute;
    left: 0;
    right: 0;
    top: 228px;
    margin: 0;
    text-align: center;
    font-size: 68px;
    font-weight: 400;
    line-height: 1;
    color: var(--card-white);
    letter-spacing: 3px;
    text-transform: uppercase;
  }
</style>
</head>
<body>
<main class="canvas">
  <section class="card card-front" aria-label="Business card front">
    <svg class="front-band" viewBox="0 0 724 412" aria-hidden="true">
      <path d="M225 412 C 330 330, 560 300, 700 412 Z" fill="var(--brand-blue)"/>
    </svg>
    <h1 class="brand-name">Korvana</h1>
    <div class="person">
      <p class="person-name"><span class="first">Daniel</span> <span class="last">Moser</span></p>
      <p class="person-role">President</p>
    </div>
    <address class="address">12 Seefeldstrasse<br>Zurich, Switzerland 8008</address>
    <ul class="contact-list">
      <li>
        <svg class="contact-icon" viewBox="0 0 16 16" aria-hidden="true"><path d="M3.5 1 L6 1 L7 4.5 L5.3 5.8 C6.2 7.8 8.2 9.8 10.2 10.7 L11.5 9 L15 10 L15 12.5 C15 13.9 13.9 15 12.5 15 C6.7 15 1 9.3 1 3.5 C1 2.1 2.1 1 3.5 1 Z"/></svg>
        <span>044-318-2650</span>
      </li>
      <li>
        <svg class="contact-icon" viewBox="0 0 16 16" aria-hidden="true"><path d="M4.5 0.5 H11.5 A1.5 1.5 0 0 1 13 2 V14 A1.5 1.5 0 0 1 11.5 15.5 H4.5 A1.5 1.5 0 0 1 3 14 V2 A1.5 1.5 0 0 1 4.5 0.5 Z M4.8 2.3 V12.5 H11.2 V2.3 Z M7 13.3 H9 V14.5 H7 Z"/></svg>
        <span>079-462-1837</span>
      </li>
      <li>
        <svg class="contact-icon" viewBox="0 0 16 16" aria-hidden="true"><path d="M4 1 H11 L12 2.5 V6 H4 Z M1 7 H15 V13 H1 Z M3 12 H13 V15 H3 Z"/></svg>
        <span>044-318-2651</span>
      </li>
      <li>
        <svg class="contact-icon" viewBox="0 0 16 16" aria-hidden="true"><path d="M1 3.5 H15 V12.5 H1 Z M2.3 4.6 L8 8.8 L13.7 4.6 Z" fill-rule="evenodd"/></svg>
        <span>moser@korvana.com</span>
      </li>
    </ul>
    <p class="website">www.Korvana.com</p>
  </section>

  <section class="card card-back" aria-label="Business card back">
    <p class="back-wordmark">Korvana</p>
  </section>
</main>
</body>
</html>
```